Legal Campaign

A courier compavny that offer Legal services like filing/recording Court documents.

These info must be on card: Can We Help With Your Legal Services? Need Your Court documents quickly filed? .Filing/Recording in Erie, Niagara & Monroe County .Pick-up within 15-30 minutes of call .Medical records pick-up & delivery .Court-Authorized Process Servers .$9.00 Buffalo to Buffalo .Volume Discounts Call Liam Torvane@716-555-0148 The address must be 47 Harlow Ave., Buffalo NY 14209

Please add the following info: 1.Post Office Pickup/Deliveries 2. Liamtorvane@brisktrn.com

Target Market(s)

Law firms & legal community.

Industry/Entity Type

Court

Requirements
Must have
• SwiftHaulo logo must be on card. Please visit the website@brisktrn.com to check out the logo. Thanks

```html
<!DOCTYPE html>
<html lang="en">
<head>
<meta charset="utf-8">
<title>SwiftHaulo Couriers – Legal Campaign Postcard</title>
<link rel="stylesheet" href="https://fonts.googleapis.com/css2?family=Montserrat:wght@500;600;700;800&family=Roboto+Condensed:wght@400;700&display=swap">
<style>
  :root{
    --orange:#f7941d;
    --blue:#0f5496;
    --blue-bright:#0a6cc2;
    --ink:#1d1d1d;
    --bg:#ececec;
    --paper:#ffffff;
    --rule:#8a8a8a;
    --logo-grey:#6d6e71;
  }
  *{margin:0;padding:0;box-sizing:border-box}
  html,body{width:1200px;height:1000px;overflow:hidden}
  body{background:var(--bg);position:relative;font-family:"Montserrat",sans-serif}

  .postcard{position:absolute;width:503px;height:389px;background:var(--paper);overflow:hidden}
  .postcard--front{left:274px;top:87px}
  .postcard--back{left:491px;top:515px}
  .abs{position:absolute}

  /* front */
  .headline-band{left:0;top:0;width:503px;height:65px;background:var(--orange);
    padding:9px 0 0 18px;color:#fff;font-family:"Roboto Condensed",sans-serif;font-weight:700;
    font-size:21px;line-height:25px;text-transform:uppercase;letter-spacing:.1px}
  .county-band{left:0;top:65px;width:345px;height:28px;background:var(--blue);color:#fff;
    font-family:"Roboto Condensed",sans-serif;font-size:13.5px;padding:5px 0 0 18px}
  .courier-figure{left:40px;top:95px;width:220px;height:220px;border-radius:50%;
    background:radial-gradient(circle,rgba(200,200,200,.35) 0%,rgba(220,220,220,0) 70%)}
  .legal-photo{left:286px;top:65px;width:217px;height:256px}
  .pickup-line{left:18px;top:106px;font-weight:700;font-size:11.5px;color:var(--blue-bright);text-transform:uppercase;white-space:nowrap}
  .pickup-line em{font-style:normal;color:var(--orange);font-size:15px}
  .route-arc{left:60px;top:118px;width:150px;height:80px;overflow:visible}
  .price{left:94px;top:146px;font-weight:800;font-size:40px;color:var(--orange);letter-spacing:.5px}
  .services{left:2px;top:199px;width:300px;text-align:center;font-weight:700;font-size:12px;line-height:18px;color:var(--ink);text-transform:uppercase}
  .volume-line{left:42px;top:245px;font-size:11.5px;color:var(--blue-bright);font-weight:500}
  .volume-line strong{font-weight:700;font-size:13px;text-transform:uppercase}
  .phone-icon{width:38px;height:38px}
  .phone-number{font-weight:700;color:var(--orange)}
  .email{font-weight:700;color:var(--blue-bright)}

  .footer-logo{left:0;background:var(--paper);display:flex;align-items:center;gap:7px;
    font-family:"Montserrat",sans-serif;font-weight:800;color:var(--logo-grey)}
  .footer-logo .mark{width:12px;height:12px;background:var(--blue);display:block}
  .footer-band{color:#fff;white-space:nowrap}
  .footer-band .company{font-weight:700}
  .footer-band .detail{font-weight:500}

  /* back */
  .web{left:70px;top:18px;font-weight:700;font-size:12px;color:var(--blue-bright)}
  .stamp-box{left:379px;top:26px;width:94px;height:98px;border:1px solid var(--rule)}
  .address-rule{left:265px;width:208px;height:1px;background:var(--rule)}
  .call-today{left:60px;top:189px;font-weight:700;font-size:12px;color:var(--blue-bright);text-transform:uppercase}
</style>
</head>
<body>

<!-- FRONT -->
<section class="postcard postcard--front" aria-label="Postcard front">
  <div class="abs courier-figure" role="img" aria-label="Faint running courier silhouette carrying a parcel"></div>

  <h1 class="abs headline-band">Can we help you with your legal service ?<br>Need your court documents quickly filed?</h1>
  <p class="abs county-band">Filing/Recording in Erie, Niagara &amp; Monroe County</p>

  <svg class="abs legal-photo" viewBox="0 0 217 256" role="img" aria-label="Photo of a stethoscope on medical papers with a gavel and a Power of Attorney document">
    <defs>
      <linearGradient id="photoTone" x1="1" y1="0" x2="0" y2="1">
        <stop offset="0" stop-color="#eef2f6"/>
        <stop offset=".45" stop-color="#c9d6e3"/>
        <stop offset=".75" stop-color="#d9cdb8"/>
        <stop offset="1" stop-color="#8b5a36"/>
      </linearGradient>
    </defs>
    <path d="M48 0 H217 V256 H12 Q0 160 28 70 Q38 28 48 0 Z" fill="url(#photoTone)"/>
  </svg>

  <p class="abs pickup-line">Pick-up within <em>15-30 minutes</em> after call</p>

  <svg class="abs route-arc" viewBox="0 0 150 80" aria-label="Buffalo to Buffalo">
    <path id="routeArc" d="M6 72 Q20 14 146 12" fill="none"/>
    <text font-family="Montserrat, sans-serif" font-weight="700" font-size="10" fill="#0a6cc2">
      <textPath href="#routeArc">BUFFALO TO BUFFALO</textPath>
    </text>
  </svg>
  <p class="abs price">$9.00</p>

  <p class="abs services">Medical record pick up &amp; delivery<br>Court-authorized process servers</p>

  <p class="abs volume-line">volume discount call <strong>Liam Torvane</strong></p>

  <svg class="abs phone-icon" style="left:26px;top:265px" viewBox="0 0 38 38" aria-hidden="true">
    <path d="M9 6 L14 5 L17 13 L13 16 Q15 23 21 27 L25 23 L32 27 L30 32 Q27 35 21 33 Q9 27 5 15 Q4 9 9 6 Z" fill="#1d1d1d"/>
    <path d="M20 9 A10 10 0 0 1 29 18" stroke="#3b6fc4" stroke-width="2.4" fill="none"/>
    <path d="M20 3 A16 16 0 0 1 35 18" stroke="#3b6fc4" stroke-width="2.4" fill="none"/>
  </svg>
  <p class="abs phone-number" style="left:69px;top:262px;font-size:25px">716-555-0148</p>
  <p class="abs email" style="left:69px;top:292px;font-size:12px">Liamtorvane@brisktrn.com</p>

  <div class="abs footer-logo" style="top:321px;width:182px;height:68px;padding-left:18px;font-size:20px">
    <span class="mark"></span>SwiftHaulo
  </div>
  <svg class="abs" style="left:166px;top:321px" width="337" height="68" viewBox="0 0 337 68" aria-hidden="true">
    <polygon points="14,0 337,0 337,68 20,68 0,34" fill="#0f5496"/>
  </svg>
  <div class="abs footer-band" style="left:194px;top:328px">
    <p class="company" style="font-size:14.5px">SwiftHaulo Couriers</p>
    <p class="detail" style="font-size:10.5px;margin-top:3px">47 Harlow Ave., Buffalo NY 14209 | Phone: 716-555-0148</p>
    <p class="detail" style="font-size:10.5px;margin-top:1px">Email: Liamtorvane@brisktrn.com |&nbsp; www.brisktrn.com</p>
  </div>
</section>

<!-- BACK -->
<section class="postcard postcard--back" aria-label="Postcard back">
  <p class="abs web">www.brisktrn.com</p>
  <div class="abs stamp-box"></div>
  <div class="abs address-rule" style="top:154px"></div>
  <div class="abs address-rule" style="top:181px"></div>
  <div class="abs address-rule" style="top:208px"></div>
  <div class="abs address-rule" style="top:234px"></div>

  <p class="abs call-today">Call us today!!</p>
  <svg class="abs phone-icon" style="left:24px;top:207px;width:34px;height:34px" viewBox="0 0 38 38" aria-hidden="true">
    <path d="M9 6 L14 5 L17 13 L13 16 Q15 23 21 27 L25 23 L32 27 L30 32 Q27 35 21 33 Q9 27 5 15 Q4 9 9 6 Z" fill="#1d1d1d"/>
    <path d="M20 9 A10 10 0 0 1 29 18" stroke="#3b6fc4" stroke-width="2.4" fill="none"/>
    <path d="M20 3 A16 16 0 0 1 35 18" stroke="#3b6fc4" stroke-width="2.4" fill="none"/>
  </svg>
  <p class="abs phone-number" style="left:61px;top:204px;font-size:22px">716-555-0148</p>
  <p class="abs email" style="left:62px;top:230px;font-size:11px">Liamtorvane@brisktrn.com</p>

  <div class="abs footer-logo" style="top:260px;width:160px;height:58px;padding-left:14px;font-size:17px">
    <span class="mark" style="width:10px;height:10px"></span>SwiftHaulo
  </div>
  <svg class="abs" style="left:141px;top:260px" width="324" height="58" viewBox="0 0 324 58" aria-hidden="true">
    <polygon points="18,0 324,0 309,29 324,58 18,58 0,29" fill="#0f5496"/>
  </svg>
  <div class="abs footer-band" style="left:176px;top:266px">
    <p class="company" style="font-size:13px">SwiftHaulo Couriers</p>
    <p class="detail" style="font-size:9.5px;margin-top:3px">47 Harlow Ave., Buffalo NY 14209 | Phone: 716-555-0148</p>
    <p class="detail" style="font-size:9.5px;margin-top:1px">Email: Liamtorvane@brisktrn.com | www.brisktrn.com</p>
  </div>
</section>

</body>
</html>
```